Would like to reproduce this screen to look more modern

My app is a place for farmers to post jobs a when needing help around the Farm, and local farmhands can apply for the job. The Farmer can then review multiple applicants and select the one best fit for the task at hand. I'm trying to give my screens an updated look while keeping my current color scheme and flow. I would like for you guys to recreate this screen with an updated look the best you can. The main screen with the BV will stay the same. I put that in there to show our logo and our main colors. They look outdated. the other 2 screens are looking at the customers profile, and the screen that u fill out to post a new job.

Target Market(s)

Farmers and farm employees inside the US

Industry/Entity Type

Agriculture

Requirements
Must have
• the same components for the flow but a new look
Nice to have
• ...
Should not have
• Should not change any features, but we can change how buttons look

```html
<!DOCTYPE html>
<html lang="en">
<head>
<meta charset="utf-8">
<title>Farm Jobs – Home</title>
<link href="https://fonts.googleapis.com/css2?family=Inter:wght@400;500;600;700&display=swap" rel="stylesheet">
<style>
  :root {
    --bg: #e1f5e1;
    --green-light: #7cb152;
    --green-dark: #5c8f40;
    --accent: #7cc05a;
    --panel: #f4f4f4;
    --card: #ffffff;
    --ink: #1f1f1f;
    --muted: #8a8a8a;
    --faint: #b3b3b3;
    --price: #3f3f3f;
    --heart: #ef4040;
    --heart-off: #e6e6e6;
    --orange: #f0913a; --orange-bg: #fff3ea;
    --red: #e34848; --red-bg: #fff0ef;
    --blue: #3d9be9; --blue-bg: #eef5fd;
    --purple: #9c27b0; --purple-bg: #f4f2fa;
  }
  * { box-sizing: border-box; margin: 0; padding: 0; }
  html, body { width: 949px; height: 1200px; overflow: hidden; }
  body { background: var(--bg); font-family: 'Inter', sans-serif; color: var(--ink); position: relative; }

  .screen {
    position: absolute; left: 213px; top: 36px; width: 522px; height: 1128px;
    border-radius: 48px; overflow: hidden; background: var(--panel);
  }
  .header {
    position: absolute; inset: 0 0 auto 0; height: 290px;
    background: linear-gradient(160deg, var(--green-light), var(--green-dark));
  }
  .avatar {
    position: absolute; left: 26px; top: 46px; width: 56px; height: 56px; border-radius: 50%;
    background: linear-gradient(160deg, #d9d9d9, #7a7a7a); border: 3px solid #fff;
    box-shadow: 0 4px 10px rgba(0,0,0,.25);
  }
  .user-name { position: absolute; left: 94px; top: 52px; color: #fff; font-size: 22px; font-weight: 700; letter-spacing: -.3px; }
  .user-phone { position: absolute; left: 94px; top: 80px; color: #fff; font-size: 14px; }
  .icon-bell { position: absolute; left: 430px; top: 58px; }
  .icon-menu { position: absolute; left: 480px; top: 64px; }
  .post-job {
    position: absolute; left: 153px; top: 150px; width: 216px; height: 58px; border-radius: 29px;
    background: #fff; color: var(--ink); font-size: 20px; font-weight: 600; border: none;
    box-shadow: 0 6px 14px rgba(0,0,0,.15); font-family: inherit; letter-spacing: -.2px;
  }
  .panel {
    position: absolute; left: 0; top: 254px; width: 522px; height: 874px;
    background: var(--panel); border-radius: 32px 32px 0 0; overflow: hidden;
  }
  .tab { position: absolute; top: 22px; font-size: 19px; font-weight: 600; letter-spacing: -.3px; }
  .tab-active { left: 33px; color: var(--ink); }
  .tab-inactive { left: 286px; color: var(--faint); }
  .tab-underline { position: absolute; left: 66px; top: 55px; width: 104px; height: 4px; border-radius: 2px; background: var(--accent); }
  .search {
    position: absolute; left: 21px; top: 84px; width: 442px; height: 56px; border-radius: 28px;
    background: #fff; display: flex; align-items: center; gap: 10px; padding-left: 24px;
    color: var(--faint); font-size: 18px;
  }
  .filter { position: absolute; left: 476px; top: 98px; }
  .job-card {
    position: absolute; left: 21px; width: 481px; height: 141px; border-radius: 18px;
    background: var(--card); box-shadow: 0 2px 6px rgba(0,0,0,.04);
  }
  .date-box {
    position: absolute; left: 12px; top: 12px; width: 104px; height: 116px; border-radius: 14px;
    display: flex; flex-direction: column; align-items: center; justify-content: center;
    font-weight: 600; gap: 4px;
  }
  .date-box .date { font-size: 19px; letter-spacing: -.3px; }
  .date-box .to { font-size: 12px; font-weight: 700; }
  .date-orange { background: var(--orange-bg); color: var(--orange); }
  .date-red { background: var(--red-bg); color: var(--red); }
  .date-blue { background: var(--blue-bg); color: var(--blue); }
  .date-purple { background: var(--purple-bg); color: var(--purple); }
  .job-title { position: absolute; left: 128px; top: 18px; font-size: 17px; font-weight: 600; letter-spacing: -.3px; }
  .meta { position: absolute; left: 128px; display: flex; align-items: center; gap: 8px; font-size: 14.5px; color: var(--muted); }
  .meta svg { width: 10px; height: 10px; fill: var(--muted); }
  .meta-1 { top: 48px; } .meta-2 { top: 75px; } .meta-3 { top: 102px; }
  .price { position: absolute; right: 20px; top: 44px; width: 100px; text-align: center; }
  .price strong { display: block; font-size: 27px; font-weight: 600; color: var(--price); letter-spacing: -.5px; }
  .price span { display: block; font-size: 14px; color: var(--muted); margin-top: 4px; }
  .heart { position: absolute; left: 450px; top: 8px; }
  .bottom-nav {
    position: absolute; left: 0; top: 1030px; width: 522px; height: 98px; background: #fff;
    border-radius: 28px 28px 0 0;
  }
  .nav-icon { position: absolute; top: 26px; }
  .home-indicator { position: absolute; left: 172px; top: 83px; width: 177px; height: 7px; border-radius: 4px; background: #111; }
</style>
</head>
<body>
<main class="screen">
  <header class="header">
    <div class="avatar" role="img" aria-label="Profile photo of the farmer"></div>
    <div class="user-name">Daniel Hartwell</div>
    <div class="user-phone">5550142876</div>
    <svg class="icon-bell" width="28" height="30" viewBox="0 0 28 30" fill="none" stroke="#fff" stroke-width="1.8" stroke-linecap="round">
      <path d="M6 21V13a8 8 0 0 1 16 0v8l2 2H4z"/><path d="M11 26a3 3 0 0 0 6 0"/>
      <circle cx="22" cy="4" r="3" fill="var(--heart)" stroke="none"/>
    </svg>
    <svg class="icon-menu" width="24" height="14" viewBox="0 0 24 14" stroke="#fff" stroke-width="2" stroke-linecap="round">
      <line x1="4" y1="2" x2="22" y2="2"/><line x1="10" y1="12" x2="22" y2="12"/>
    </svg>
    <button class="post-job">POST NEW JOB</button>
  </header>

  <section class="panel">
    <div class="tab tab-active">Current Jobs For You</div>
    <div class="tab tab-inactive">Nearby Farmhands</div>
    <div class="tab-underline"></div>

    <div class="search">
      <svg width="16" height="16" viewBox="0 0 16 16" fill="none" stroke="#9a9a9a" stroke-width="1.6"><circle cx="7" cy="7" r="5.5"/><line x1="11" y1="11" x2="15" y2="15"/></svg>
      Search
    </div>
    <svg class="filter" width="26" height="26" viewBox="0 0 26 26" fill="none" stroke="#3f7a2c" stroke-width="1.6">
      <line x1="1" y1="4" x2="25" y2="4"/><rect x="7" y="1" width="4" height="6" fill="var(--panel)"/>
      <line x1="1" y1="13" x2="25" y2="13"/><rect x="14" y="10" width="4" height="6" fill="var(--panel)"/>
      <line x1="1" y1="22" x2="25" y2="22"/><rect x="7" y="19" width="4" height="6" fill="var(--panel)"/>
    </svg>

    <article class="job-card" style="top:160px">
      <div class="date-box date-orange"><span class="date">01 APR</span><span class="to">— TO —</span><span class="date">15 APR</span></div>
      <h3 class="job-title">Seasonal Farm Labor</h3>
      <div class="meta meta-1"><svg viewBox="0 0 10 10"><path d="M5 0a3.5 3.5 0 0 1 3.5 3.5C8.5 6 5 10 5 10S1.5 6 1.5 3.5A3.5 3.5 0 0 1 5 0z"/></svg>Dewitt, Iowa</div>
      <div class="meta meta-2"><svg viewBox="0 0 10 10"><path d="M3 1h4l3 8H0z"/></svg>2.92 miles</div>
      <div class="meta meta-3"><svg viewBox="0 0 10 10"><circle cx="5" cy="5" r="5"/></svg>08:00 am - 08:00 pm</div>
      <div class="price"><strong>$12-20</strong><span>Hourly Rate</span></div>
      <svg class="heart" width="20" height="18" viewBox="0 0 20 18"><path fill="var(--heart)" d="M10 18 1.5 9.5A5 5 0 0 1 10 3a5 5 0 0 1 8.5 6.5z"/></svg>
    </article>

    <article class="job-card" style="top:336px">
      <div class="date-box date-red"><span class="date">16 OCT</span><span class="to">— TO —</span><span class="date">18 OCT</span></div>
      <h3 class="job-title">Farm Hand, Sprayer, Truck, Repair</h3>
      <div class="meta meta-1"><svg viewBox="0 0 10 10"><path d="M5 0a3.5 3.5 0 0 1 3.5 3.5C8.5 6 5 10 5 10S1.5 6 1.5 3.5A3.5 3.5 0 0 1 5 0z"/></svg>Alabaster, Alabama</div>
      <div class="meta meta-2"><svg viewBox="0 0 10 10"><path d="M3 1h4l3 8H0z"/></svg>5118 miles</div>
      <div class="meta meta-3"><svg viewBox="0 0 10 10"><circle cx="5" cy="5" r="5"/></svg>06:00 am - 05:00 pm</div>
      <div class="price"><strong>$25-30</strong><span>Hourly Rate</span></div>
      <svg class="heart" width="20" height="18" viewBox="0 0 20 18"><path fill="var(--heart-off)" d="M10 18 1.5 9.5A5 5 0 0 1 10 3a5 5 0 0 1 8.5 6.5z"/></svg>
    </article>

    <article class="job-card" style="top:512px">
      <div class="date-box date-blue"><span class="date">04 NOV</span><span class="to">— TO —</span><span class="date">06 NOV</span></div>
      <h3 class="job-title">Running tillage Tractor</h3>
      <div class="meta meta-1"><svg viewBox="0 0 10 10"><path d="M5 0a3.5 3.5 0 0 1 3.5 3.5C8.5 6 5 10 5 10S1.5 6 1.5 3.5A3.5 3.5 0 0 1 5 0z"/></svg>Dewitt, Iowa</div>
      <div class="meta meta-2"><svg viewBox="0 0 10 10"><path d="M3 1h4l3 8H0z"/></svg>891 miles</div>
      <div class="meta meta-3"><svg viewBox="0 0 10 10"><circle cx="5" cy="5" r="5"/></svg>10:00 am - 05:00 pm</div>
      <div class="price"><strong>$17-25</strong><span>Hourly Rate</span></div>
      <svg class="heart" width="20" height="18" viewBox="0 0 20 18"><path fill="var(--heart)" d="M10 18 1.5 9.5A5 5 0 0 1 10 3a5 5 0 0 1 8.5 6.5z"/></svg>
    </article>

    <article class="job-card" style="top:688px">
      <div class="date-box date-purple"><span class="date">16 OCT</span><span class="to">— TO —</span><span class="date">18 OCT</span></div>
      <h3 class="job-title">Loading 2 loads of Cattle</h3>
      <div class="meta meta-1"><svg viewBox="0 0 10 10"><path d="M5 0a3.5 3.5 0 0 1 3.5 3.5C8.5 6 5 10 5 10S1.5 6 1.5 3.5A3.5 3.5 0 0 1 5 0z"/></svg>Dewitt, Iowa</div>
      <div class="meta meta-2"><svg viewBox="0 0 10 10"><path d="M3 1h4l3 8H0z"/></svg>891 miles</div>
      <div class="meta meta-3"><svg viewBox="0 0 10 10"><circle cx="5" cy="5" r="5"/></svg>10:00 am - 05:00 pm</div>
      <div class="price"><strong>$15-20</strong><span>Hourly Rate</span></div>
      <svg class="heart" width="20" height="18" viewBox="0 0 20 18"><path fill="var(--heart-off)" d="M10 18 1.5 9.5A5 5 0 0 1 10 3a5 5 0 0 1 8.5 6.5z"/></svg>
    </article>
  </section>

  <nav class="bottom-nav">
    <svg class="nav-icon" style="left:49px" width="28" height="28" viewBox="0 0 28 28" stroke="#1f1f1f" stroke-width="1.8" stroke-linejoin="round">
      <path d="M3 13 14 3l11 10v12H3z" fill="var(--green-light)"/><rect x="11" y="17" width="6" height="8" fill="#fff"/>
    </svg>
    <svg class="nav-icon" style="left:150px" width="28" height="28" viewBox="0 0 28 28" fill="none" stroke="#aaa" stroke-width="1.8" stroke-linecap="round">
      <circle cx="11" cy="11" r="8"/><line x1="17" y1="17" x2="26" y2="26"/>
    </svg>
    <svg class="nav-icon" style="left:250px" width="28" height="28" viewBox="0 0 28 28" fill="none" stroke="#aaa" stroke-width="1.8">
      <rect x="2" y="3" width="24" height="22" rx="3"/><line x1="6" y1="9" x2="22" y2="9"/><line x1="6" y1="14" x2="22" y2="14"/><line x1="6" y1="19" x2="16" y2="19"/>
    </svg>
    <svg class="nav-icon" style="left:349px" width="28" height="28" viewBox="0 0 28 28" fill="none" stroke="#aaa" stroke-width="1.6" stroke-linecap="round">
      <path d="M8 16V7a1.5 1.5 0 0 1 3 0v7M11 13V4a1.5 1.5 0 0 1 3 0v9M14 13V5a1.5 1.5 0 0 1 3 0v9M17 14V8a1.5 1.5 0 0 1 3 0v9c0 5-3 9-7 9s-6-3-8-7l-2-4a1.5 1.5 0 0 1 3-1l2 3"/>
    </svg>
    <svg class="nav-icon" style="left:445px" width="28" height="28" viewBox="0 0 28 28" fill="none" stroke="#aaa" stroke-width="1.6">
      <rect x="2" y="4" width="24" height="22" rx="3"/><line x1="2" y1="10" x2="26" y2="10"/><line x1="8" y1="1" x2="8" y2="6"/><line x1="20" y1="1" x2="20" y2="6"/>
      <g fill="#aaa" stroke="none"><circle cx="8" cy="15" r="1.2"/><circle cx="12" cy="15" r="1.2"/><circle cx="16" cy="15" r="1.2"/><circle cx="20" cy="15" r="1.2"/><circle cx="8" cy="20" r="1.2"/><circle cx="12" cy="20" r="1.2"/><circle cx="16" cy="20" r="1.2"/><circle cx="20" cy="20" r="1.2"/></g>
    </svg>
    <div class="home-indicator"></div>
  </nav>
</main>
</body>
</html>
```